Brightmere Business Card Redesign & Logo Update

We need to update our business cards to something more modern and fresh. Brightmere can provide the current color schemes and old design examples, but welcome creativity in helping us with this redesign. PLEASE NOTE that we no longer utilize the "tree" and/or "leaf" imagery in our branding. If able would apprecaite an update on the quality of our "words only" logo in Ai. / PNG formats too.

Target Market(s)

Investors, landowners, corporate partners, contractors

Industry/Entity Type

Environmental Restoration & Conservation

Contact Information for Business Card

Logo, persons name, title, mailing address, phone and email, website url

Font styles to use
Other font styles liked:
• Merriweather

Requirements
Nice to have
• Logo, persons name, title, mailing address, phone and email, website url, but open to ideams
Should not have
• No all back backgrounds

```html
<!DOCTYPE html>
<html lang="en">
<head>
<meta charset="utf-8">
<title>Brightmere Business Card</title>
<link href="https://fonts.googleapis.com/css2?family=Oswald:wght@600&family=Lato:wght@400;700&display=swap" rel="stylesheet">
<style>
  :root {
    --bg: #1f1f1f;
    --paper: #ffffff;
    --orange: #ef7d00;
    --green: #137d38;
    --ink: #111111;
    --muted: #444444;
  }
  * { box-sizing: border-box; margin: 0; padding: 0; }
  html, body { width: 1200px; height: 1015px; overflow: hidden; }
  body {
    background: var(--bg);
    position: relative;
    font-family: "Lato", sans-serif;
  }
  .card {
    position: absolute;
    width: 560px;
    height: 320px;
    overflow: hidden;
    background: var(--paper);
    box-shadow: 0 10px 30px rgba(0,0,0,.55);
  }
  .card--back { left: 80px; top: 110px; }
  .card--front { left: 560px; top: 580px; }

  .brand { position: absolute; left: 0; right: 0; text-align: center; }
  .brand__name {
    display: flex;
    align-items: center;
    justify-content: center;
    gap: 14px;
    font-weight: 700;
    font-size: 52px;
    line-height: 1;
    color: var(--green);
  }
  .brand__mark {
    width: 18px; height: 18px;
    border-radius: 50%;
    background: var(--orange);
    flex: none;
  }
  .brand__tagline {
    display: block;
    font-weight: 400;
    font-size: 16px;
    color: var(--muted);
    margin-top: 10px;
  }
  .card--back .brand { top: 104px; }
  .card--front .brand { top: 30px; }
  .card--front .brand__name { font-size: 46px; }
  .card--front .brand__tagline { font-size: 15px; margin-top: 8px; }

  .back-stripes { position: absolute; left: 0; right: 0; bottom: 0; }
  .back-stripes__orange { height: 14px; background: var(--orange); }
  .back-stripes__green { height: 14px; background: var(--green); }

  .band-orange {
    position: absolute; left: 0; right: 0; top: 150px; height: 110px;
    background: var(--orange);
    display: flex; align-items: center;
    color: var(--paper);
  }
  .person { width: 270px; text-align: right; padding-right: 24px; }
  .person__name {
    font-family: "Oswald", sans-serif; font-weight: 600;
    font-size: 30px; line-height: 1.05; text-transform: uppercase;
  }
  .person__title { font-size: 17px; }
  .divider { width: 1px; height: 74px; background: rgba(255,255,255,.5); }
  .contacts { list-style: none; padding-left: 22px; font-size: 16px; line-height: 1.6; }
  .contacts li { display: flex; align-items: center; gap: 9px; }
  .contacts svg { width: 16px; height: 16px; flex: none; }

  .band-green {
    position: absolute; left: 0; right: 0; bottom: 0; height: 60px;
    background: var(--green);
    color: var(--paper);
    font-size: 17px;
    display: flex; align-items: center; justify-content: center;
  }
</style>
</head>
<body>

  <section class="card card--back">
    <div class="brand">
      <span class="brand__name"><span class="brand__mark"></span>Brightmere</span>
      <span class="brand__tagline">Environmental Credit Company</span>
    </div>
    <div class="back-stripes">
      <div class="back-stripes__orange"></div>
      <div class="back-stripes__green"></div>
    </div>
  </section>

  <section class="card card--front">
    <div class="brand">
      <span class="brand__name"><span class="brand__mark"></span>Brightmere</span>
      <span class="brand__tagline">Environmental Credit Company</span>
    </div>

    <div class="band-orange">
      <div class="person">
        <p class="person__name">Daniel Hart</p>
        <p class="person__title">Managing Director</p>
      </div>
      <div class="divider"></div>
      <ul class="contacts">
        <li>
          <svg viewBox="0 0 16 16" aria-hidden="true"><path d="M3.5 1.5l2.5 2.8-1.3 1.7c.9 2 2.4 3.5 4.3 4.4l1.7-1.3 2.8 2.5-1.4 2.2C7 13.5 2.4 9 1.5 3z" fill="#fff"/></svg>
          044-555 010 246
        </li>
        <li>
          <svg viewBox="0 0 16 16" aria-hidden="true"><rect x="1" y="3.5" width="14" height="9" fill="none" stroke="#fff" stroke-width="1.5"/><path d="M1 3.5l7 5.5 7-5.5" fill="none" stroke="#fff" stroke-width="1.5"/></svg>
          hello@brightmere.co
        </li>
        <li>
          <svg viewBox="0 0 16 16" aria-hidden="true"><g fill="none" stroke="#fff" stroke-width="1.3"><circle cx="8" cy="8" r="6.5"/><ellipse cx="8" cy="8" rx="3" ry="6.5"/><path d="M1.5 8h13M2.5 4.8h11M2.5 11.2h11"/></g></svg>
          www.brightmere.co
        </li>
      </ul>
    </div>

    <p class="band-green">88, Fernhill Road, Ashford Vale, 30917</p>
  </section>

</body>
</html>
```